Startup online payment business - Sporting / Golf, Swift Tee payment

Background:
Our business name is "Swift Tee" we provide online payments for golfing services via our website. We currently have a logo used on our website. No other design style has been developed. Our aim is to remove cash payments for service at golf clubs.

Our Key Values:
Quick and easy
Formal and polite
Fun with professional boundary
Mate-ship relationships
100% online digital

What we want from you:
Marketing design to be used on posters and stickers in a retail setting to direct customers to our online payment Chanel.
Design must incorporate attached logo, URL swifttee.com.au and our key values can act as a guide the type of design. We have used color Hex#007672 for logo background. We are open to use other colors.

Target Market(s)

Golf clubs and golf players

Industry/Entity Type

Golf Course

Font styles to use
Sans Serif

Requirements
Must have
• Directions to online payment via URL: swifttee.com.au
Nice to have
• We like the idea of the slogan: No Cash - No worries. Have attached home screen that will be available from URL link. Consideration if using mobile phone in image. Push the online payment and steps 1. Visit swifttee.com 2. Select club 3. Confirm payment
Should not have
• Cartoons

```html
<!DOCTYPE html>
<html lang="en">
<head>
<meta charset="utf-8">
<title>Swift Tee – No Cash, No Worries Poster</title>
<link href="https://fonts.googleapis.com/css2?family=Jost:wght@400;500;700&display=swap" rel="stylesheet">
<style>
  :root {
    --brand-teal: #077872;
    --ink: #0b0b0b;
    --paper: #ffffff;
    --backdrop: #cfcfcf;
  }
  * { margin: 0; padding: 0; box-sizing: border-box; }
  html, body {
    width: 1200px;
    height: 1200px;
    overflow: hidden;
    background: var(--backdrop);
    font-family: "Jost", sans-serif;
  }
  .poster {
    position: absolute;
    left: 247px;
    top: 101px;
    width: 706px;
    height: 998px;
    background: var(--paper);
  }
  .poster__header {
    position: absolute;
    left: 0;
    top: 0;
    width: 100%;
    height: 564px;
    background: var(--brand-teal);
    display: flex;
    align-items: center;
    justify-content: center;
  }
  .brand-name {
    color: var(--paper);
    font-family: "Jost", sans-serif;
    font-weight: 500;
    font-size: 104px;
    letter-spacing: 6px;
    text-transform: uppercase;
    line-height: 1;
    margin-top: -20px;
  }
  .slogan {
    position: absolute;
    left: 0;
    top: 608px;
    width: 100%;
    text-align: center;
    font-weight: 700;
    font-size: 66px;
    letter-spacing: -1.5px;
    line-height: 1;
    color: var(--ink);
    white-space: nowrap;
  }
  .slogan__accent { color: var(--brand-teal); }
  .values {
    position: absolute;
    list-style: none;
    top: 726px;
    font-size: 28px;
    font-weight: 400;
    color: var(--ink);
    line-height: 41.5px;
  }
  .values li::before {
    content: "•";
    display: inline-block;
    width: 22px;
  }
  .values--left { left: 20px; }
  .values--right { left: 455px; }
  .web-link {
    position: absolute;
    left: 0;
    top: 929px;
    width: 100%;
    display: flex;
    align-items: center;
    justify-content: center;
    gap: 10px;
    color: var(--brand-teal);
    font-weight: 500;
    font-size: 25px;
    text-decoration: none;
  }
  .web-link svg { width: 34px; height: 34px; }
</style>
</head>
<body>
  <main class="poster">
    <header class="poster__header">
      <div class="brand-name">Swift Tee</div>
    </header>

    <h1 class="slogan">No <span class="slogan__accent">Cash</span> - No <span class="slogan__accent">Worries</span></h1>

    <ul class="values values--left">
      <li>Fun with professional boundary</li>
      <li>Mate-ship relationships</li>
      <li>100% online digital</li>
    </ul>
    <ul class="values values--right">
      <li>Quick and easy</li>
      <li>Formal and polite</li>
    </ul>

    <a class="web-link" href="https://swifttee.com.au/">
      <svg viewBox="0 0 34 34" aria-hidden="true">
        <circle cx="17" cy="17" r="16" fill="var(--brand-teal)"/>
        <g fill="none" stroke="#ffffff" stroke-width="1.6">
          <ellipse cx="17" cy="17" rx="7" ry="15"/>
          <line x1="17" y1="2" x2="17" y2="32"/>
          <line x1="2" y1="17" x2="32" y2="17"/>
          <path d="M5 9.5h24M5 24.5h24"/>
        </g>
      </svg>
      <span>https://swifttee.com.au/</span>
    </a>
  </main>
</body>
</html>
```